Business Card Design Project

We need a business card design for an existing company in Dallas/Fort Worth that is expanding services and re-branding. We are changing the name from Brightmoor Commercial Cleaning to Keystride Facility Services. We are expanding from only commercial cleaning to include complete commercial landscape and facility maintenance services, too.

As stated, we offer a package of services that includes landscape, janitorial and facility services, which is largely unique in the industry.

We would like a design that communicates trust/partnership with a professional, corporate image, but not necessarily using the standard white business card. We would like a design that perhaps uses darker blues or perhaps a gray background, but we are open to other ideas. We might also be interested in a double-sided design - maybe with our logo on the back, printed on a gray background?

We will probably stick with the attached logo, but if you've got another inspired idea....

Target Market(s)

Property managers, commercial real estate professionals, corporate executives

Industry/Entity Type

Landscape

Requirements
Should not have
• Not interested in old style fonts.

```html
<!DOCTYPE html>
<html lang="en">
<head>
<meta charset="utf-8">
<title>Keystride Facility Services – Business Card</title>
<link rel="stylesheet" href="https://fonts.googleapis.com/css2?family=Questrial&family=Arimo:wght@400;700&display=swap">
<style>
  :root {
    --card-bg: #201c1a;
    --band-bg: #3a3633;
    --accent-shape: #3a3633;
    --ink: #ffffff;
  }
  * { margin: 0; padding: 0; box-sizing: border-box; }
  html, body {
    width: 960px;
    height: 1200px;
    overflow: hidden;
    background: var(--card-bg);
  }
  .card {
    position: relative;
    width: 960px;
    height: 1200px;
    background: var(--card-bg);
    color: var(--ink);
    overflow: hidden;
  }
  .brand {
    position: absolute;
    left: 0;
    top: 245px;
    width: 960px;
    display: flex;
    justify-content: center;
    align-items: center;
    gap: 34px;
  }
  .brand-name {
    font-family: "Questrial", sans-serif;
    font-weight: 400;
    color: var(--ink);
    text-align: right;
    line-height: 1;
  }
  .brand-name .primary {
    display: block;
    font-size: 84px;
    letter-spacing: 4px;
  }
  .brand-name .secondary {
    display: block;
    font-size: 33px;
    letter-spacing: 2px;
    margin-top: 12px;
  }
  .brand-mark {
    width: 96px;
    height: 96px;
    border-radius: 50%;
    background: var(--accent-shape);
    flex: none;
  }
  .tagline-band {
    position: absolute;
    left: 0;
    top: 422px;
    width: 960px;
    height: 40px;
    background: var(--band-bg);
    display: flex;
    align-items: center;
    justify-content: center;
    font-family: "Questrial", sans-serif;
    font-size: 23px;
    color: var(--ink);
  }
  .website {
    position: absolute;
    left: 0;
    top: 664px;
    width: 960px;
    text-align: center;
    font-family: "Arimo", sans-serif;
    font-weight: 700;
    font-size: 26px;
    letter-spacing: 1px;
    color: var(--ink);
  }
  .contact-accent {
    position: absolute;
    left: -40px;
    top: 824px;
    width: 188px;
    height: 126px;
    border-radius: 50%;
    background: var(--accent-shape);
  }
  .contact {
    position: absolute;
    left: 173px;
    top: 845px;
    font-family: "Arimo", sans-serif;
    color: var(--ink);
  }
  .contact-name {
    font-weight: 700;
    font-size: 34px;
    line-height: 1.2;
  }
  .contact-title {
    font-weight: 400;
    font-size: 29px;
    line-height: 1.2;
    margin-left: -3px;
  }
</style>
</head>
<body>
  <div class="card">
    <div class="brand">
      <div class="brand-name">
        <span class="primary">KEYSTRIDE</span>
        <span class="secondary">FACILITY SERVICES</span>
      </div>
      <div class="brand-mark"></div>
    </div>

    <div class="tagline-band">One source for Landscape, Janitorial and Facility Maintenance</div>

    <div class="website">www.keystridefacilityservices.com</div>

    <div class="contact-accent"></div>
    <div class="contact">
      <div class="contact-name">Mark Ellison</div>
      <div class="contact-title">General Manager</div>
    </div>
  </div>
</body>
</html>
```